Wills & Estate Planning *

I have my own logo, just looking for a nice eye catching background with good quality.

Could we find a place for 'We give you the peace of mind you deserve'
Updates

Could we find somewhere on the card to put 'We give you the peace of mind you deserve' Thanks.

Target Market(s)

40+ age

Industry/Entity Type

Law Firm

Contact Information for Business Card

Lionel Hartcombe
01632 960381
admin@galvinmerecourt.co.uk
www.galvinmerecourt.co.uk

Requirements
Must have
• Please use my logo attached on the brief

```html
<!DOCTYPE html>
<html lang="en">
<head>
<meta charset="utf-8">
<title>Galvinmere Court – Business Card</title>
<link rel="stylesheet" href="https://fonts.googleapis.com/css2?family=Arimo:wght@400;700&display=swap">
<style>
  :root {
    --backdrop: #e4e5e8;
    --card-blue: #2c4a8c;
    --card-blue-dark: #223c76;
    --card-white: #ffffff;
    --navy: #24407f;
    --slate: #5f6470;
    --ink: #1e1e22;
    --front-text: #e9ecf2;
    --front-muted: #c3cbe0;
  }
  * { margin: 0; padding: 0; box-sizing: border-box; }
  html, body {
    width: 1200px;
    height: 997px;
    overflow: hidden;
    background: var(--backdrop);
    font-family: "Arimo", Arial, sans-serif;
  }
  .canvas {
    width: 1200px;
    height: 997px;
    display: flex;
    flex-direction: column;
    align-items: center;
    justify-content: center;
    gap: 40px;
  }
  .card {
    width: 760px;
    height: 434px;
    border-radius: 4px;
    box-shadow: 0 10px 28px rgba(0, 0, 0, 0.18);
    position: relative;
    overflow: hidden;
  }

  .brand-name {
    font-family: "Arimo", Arial, sans-serif;
    font-weight: 400;
    letter-spacing: 0.04em;
    text-transform: uppercase;
    white-space: nowrap;
  }

  /* Front */
  .card--front {
    background: linear-gradient(135deg, var(--card-blue) 0%, var(--card-blue-dark) 100%);
    display: flex;
    flex-direction: column;
    align-items: center;
    justify-content: center;
    gap: 22px;
  }
  .card--front .brand-name {
    color: var(--front-text);
    font-size: 52px;
  }
  .tagline {
    color: var(--front-muted);
    font-size: 18px;
    font-weight: 400;
    letter-spacing: 0.03em;
    white-space: nowrap;
  }

  /* Back */
  .card--back {
    background: var(--card-white);
    display: flex;
    align-items: center;
  }
  .brand-block {
    width: 430px;
    display: flex;
    align-items: center;
    justify-content: center;
  }
  .card--back .brand-name {
    color: var(--navy);
    font-size: 34px;
  }
  .divider {
    width: 2px;
    height: 250px;
    background: linear-gradient(to bottom, rgba(36, 64, 127, 0) 0%, var(--navy) 45%, rgba(36, 64, 127, 0) 100%);
  }
  .contact-block {
    padding-left: 40px;
  }
  .person-name {
    color: var(--navy);
    font-weight: 700;
    font-size: 19px;
    text-transform: uppercase;
    letter-spacing: 0.02em;
  }
  .person-title {
    color: var(--slate);
    font-size: 15px;
    margin-top: 3px;
  }
  .contact-list {
    list-style: none;
    margin-top: 52px;
  }
  .contact-list li {
    display: flex;
    align-items: center;
    gap: 10px;
    color: var(--ink);
    font-size: 15px;
    line-height: 24px;
  }
  .contact-list svg {
    width: 11px;
    height: 11px;
    fill: var(--navy);
    flex: none;
  }
</style>
</head>
<body>
<main class="canvas">
  <section class="card card--front" aria-label="Card front">
    <span class="brand-name">Galvinmere Court</span>
    <p class="tagline">We give you the peace of mind you deserve</p>
  </section>

  <section class="card card--back" aria-label="Card back">
    <div class="brand-block">
      <span class="brand-name">Galvinmere Court</span>
    </div>
    <div class="divider"></div>
    <div class="contact-block">
      <p class="person-name">Lionel Hartcombe</p>
      <p class="person-title">Managing Director</p>
      <ul class="contact-list">
        <li>
          <svg viewBox="0 0 24 24" aria-hidden="true"><path d="M6.6 10.8a15.1 15.1 0 0 0 6.6 6.6l2.2-2.2a1 1 0 0 1 1-.25 11.4 11.4 0 0 0 3.6.57 1 1 0 0 1 1 1V20a1 1 0 0 1-1 1A17 17 0 0 1 3 4a1 1 0 0 1 1-1h3.5a1 1 0 0 1 1 1c0 1.25.2 2.45.57 3.57a1 1 0 0 1-.25 1z"/></svg>
          01632 960381
        </li>
        <li>
          <svg viewBox="0 0 24 24" aria-hidden="true"><path d="M2 5h20v2l-10 6L2 7zm0 4.3 10 6 10-6V19H2z"/></svg>
          admin@galvinmerecourt.co.uk
        </li>
        <li>
          <svg viewBox="0 0 24 24" aria-hidden="true"><path d="M12 2a7 7 0 0 0-7 7c0 5.2 7 13 7 13s7-7.8 7-13a7 7 0 0 0-7-7zm0 9.5A2.5 2.5 0 1 1 12 6.5a2.5 2.5 0 0 1 0 5z"/></svg>
          www.galvinmerecourt.co.uk
        </li>
      </ul>
    </div>
  </section>
</main>
</body>
</html>
```